Letterhead Design Project

Professional but modern letterhead.

Target Market(s)

mining companies

Industry/Entity Type

It Professional

Colors

Designer to choose colors to be used in the design.

```html
<!DOCTYPE html>
<html lang="en">
<head>
<meta charset="utf-8">
<title>KORVA Letterhead</title>
<link rel="stylesheet" href="https://fonts.googleapis.com/css2?family=Open+Sans:wght@400;600&display=swap">
<style>
  :root {
    --backdrop: #f3f3f5;
    --paper: #ffffff;
    --brand-blue: #1a3f94;
    --web-grey: #5a5a5a;
    --tint-light: #e4e7f3;
    --tint-mid: #a9b0d3;
    --tint-deep: #6b78b1;
    --footer-text: #ffffff;
    --icon-fill: #24428f;
  }
  * { margin: 0; padding: 0; box-sizing: border-box; }
  html, body {
    width: 1200px;
    height: 1200px;
    overflow: hidden;
    background: var(--backdrop);
    font-family: "Open Sans", Arial, sans-serif;
  }
  .letterhead {
    position: absolute;
    left: 182px;
    top: 60px;
    width: 835px;
    height: 1080px;
    background: var(--paper);
    overflow: hidden;
  }
  .brand {
    position: absolute;
    right: 39px;
    top: 212px;
    text-align: right;
  }
  .brand-name {
    font-weight: 600;
    font-size: 68px;
    line-height: 1;
    letter-spacing: 1px;
    color: var(--brand-blue);
  }
  .brand-web {
    margin-top: 22px;
    font-size: 13px;
    color: var(--web-grey);
    letter-spacing: 0.3px;
  }
  .footer-tint {
    position: absolute;
    left: 0;
    top: 640px;
    width: 835px;
    height: 440px;
    background: linear-gradient(160deg,
      var(--paper) 0%,
      var(--paper) 12%,
      var(--tint-light) 40%,
      var(--tint-mid) 70%,
      var(--tint-deep) 100%);
  }
  .footer {
    position: absolute;
    right: 39px;
    bottom: 40px;
    text-align: right;
    color: var(--footer-text);
  }
  .contact-line {
    display: flex;
    justify-content: flex-end;
    align-items: center;
    gap: 16px;
    font-size: 13px;
    letter-spacing: 0.2px;
  }
  .contact-item {
    display: flex;
    align-items: center;
    gap: 5px;
  }
  .contact-icon {
    width: 12px;
    height: 12px;
    display: block;
  }
  .registered-line {
    margin-top: 10px;
    font-size: 8.5px;
    letter-spacing: 2px;
    text-transform: uppercase;
    color: var(--footer-text);
  }
  .registered-line span + span { margin-left: 14px; }
</style>
</head>
<body>
  <main class="letterhead">
    <header class="brand">
      <div class="brand-name">KORVA</div>
      <div class="brand-web">www.korvagroup.com</div>
    </header>

    <div class="footer-tint" role="img" aria-label="Soft blue decorative wave area along the bottom of the page"></div>

    <footer class="footer">
      <div class="contact-line">
        <span class="contact-item">Suite #410, Crest Bldg, NY 10452</span>
        <span class="contact-item">
          <svg class="contact-icon" viewBox="0 0 12 12" aria-hidden="true">
            <circle cx="6" cy="6" r="6" fill="var(--icon-fill)"/>
            <path d="M4 3 L5.2 4.4 L4.6 5.2 C5 6.2 5.8 7 6.8 7.4 L7.6 6.8 L9 8 L8.2 9 C5.8 8.8 3.2 6.2 3 3.8 Z" fill="#fff"/>
          </svg>
          555-010-2468
        </span>
        <span class="contact-item">
          <svg class="contact-icon" viewBox="0 0 12 12" aria-hidden="true">
            <circle cx="6" cy="6" r="6" fill="var(--icon-fill)"/>
            <rect x="3.5" y="3" width="5" height="2.2" fill="#fff"/>
            <rect x="2.8" y="5.6" width="6.4" height="3.4" rx="0.6" fill="#fff"/>
          </svg>
          555-010-1357
        </span>
        <span class="contact-item">
          <svg class="contact-icon" viewBox="0 0 12 12" aria-hidden="true">
            <circle cx="6" cy="6" r="6" fill="var(--icon-fill)"/>
            <rect x="3" y="4" width="6" height="4.2" fill="#fff"/>
            <path d="M3 4 L6 6.4 L9 4" fill="none" stroke="var(--icon-fill)" stroke-width="0.8"/>
          </svg>
          info@korvagroup.com
        </span>
      </div>
      <div class="registered-line">
        <span>Registered address: &nbsp;Suite # 410, Crest Bldg, NY 10452</span>
        <span>Company registration number: 987 654 3210</span>
      </div>
    </footer>
  </main>
</body>
</html>
```